Kids Bamboo sun protection clothing

We need a flyer to promote our bamboo sun protection range to parents of kids with sensitive due to illness or skin conditions.
Our clothing is made from bamboo that has been specially knitted for high sun protection but does not use chemicals. The clothing is for everyday wear, to the playground, going for walks, after a swim. Special features such as hoods, high necklines, long sleeves and thumb loops create more coverage but it is not a lycra rash vest. You can see the product at www.lumora-wear.com. We would like this flyer (or postcard) to show parents with children who are sensitive tot he sun that there is an option. Their kids might have albinism, Cancer or severe burns, might be sensitive to the sun or have Eczema. These clothes are natural fabric with styling to help look after their skin in the sun. We would like a soft caring approach.

Target Market(s)

Mums of children who have sensitive skin due to burns, cancer, Eczema or UV sensitivity.

Industry/Entity Type

Health

Font styles to use
Sans Serif

Requirements
Must have
• Point out how it can protect the skin with fabric and design features.
• Be eye catching so if it is in a waiting room at the doctors people will go over to pick it up. Be a soft approach that does not concentrate on the illness.
• Website details
Nice to have
• mention that we also do women's wear
• Please use any images off the website

```html
<!DOCTYPE html>
<html lang="en">
<head>
<meta charset="utf-8">
<title>Lumora Kids Clothing Flyer</title>
<link href="https://fonts.googleapis.com/css2?family=Didact+Gothic&family=Lato:ital,wght@0,400;0,700;1,400;1,700&display=swap" rel="stylesheet">
<style>
  :root {
    --orange: #f7a428;
    --dark: #3a3a3a;
    --ink: #1a1a1a;
    --paper: #f4f4f4;
    --stage: #d6d6d6;
  }
  * { box-sizing: border-box; margin: 0; padding: 0; }
  html, body { width: 1200px; height: 1200px; overflow: hidden; }
  body { background: var(--stage); font-family: 'Lato', sans-serif; color: var(--ink); }
  .flyer {
    position: absolute; left: 190px; top: 20px;
    width: 820px; height: 1160px;
    background: linear-gradient(135deg, #fbfbfb 0%, var(--paper) 55%, #ececec 100%);
    overflow: hidden;
    box-shadow: 0 6px 24px rgba(0,0,0,.18);
  }
  .flyer-art { position: absolute; inset: 0; }
  .brand { position: absolute; left: 70px; top: 88px; }
  .brand-rule { width: 270px; height: 4px; background: var(--orange); margin-bottom: 6px; }
  .brand-name {
    font-family: 'Didact Gothic', sans-serif; font-size: 66px; letter-spacing: 2px;
    color: #6b6b6b; line-height: 1;
  }
  .headline { position: absolute; left: 80px; top: 250px; font-family: 'Didact Gothic', sans-serif; font-weight: 400; line-height: 1; }
  .headline-top { font-size: 50px; color: var(--ink); }
  .headline-bottom { font-size: 68px; color: var(--orange); margin-top: 4px; }
  .web-ribbon {
    position: absolute; left: 0; top: 392px; width: 510px; height: 54px;
    background: var(--orange);
    clip-path: polygon(0 0, 100% 0, 92% 100%, 0 100%);
    color: #fff; font-size: 20px; font-weight: 700; letter-spacing: .5px;
    white-space: nowrap;
    display: flex; align-items: center; padding-left: 60px;
  }
  .intro { position: absolute; left: 90px; top: 478px; width: 380px; font-size: 15px; line-height: 1.4; }
  .need-box {
    position: absolute; left: 90px; top: 565px; width: 400px; height: 190px;
    border: 2px solid var(--orange); border-radius: 28px; background: rgba(255,255,255,.55);
    padding: 24px 26px; font-size: 17px; line-height: 1.35;
  }
  .need-box .lead { font-style: italic; margin-bottom: 4px; }
  .need-box ul { list-style: none; }
  .need-box li::before { content: "\25CF"; font-size: 12px; margin-right: 8px; vertical-align: 2px; }
  .need-box .close { font-style: italic; font-weight: 700; margin-top: 6px; }
  .range { position: absolute; left: 90px; top: 790px; width: 520px; font-size: 15px; line-height: 1.4; }
  .promise { position: absolute; left: 90px; top: 852px; width: 530px; font-size: 15px; line-height: 1.45; }
  .promise strong { font-weight: 700; }
  .nowrap { white-space: nowrap; }
  .features { position: absolute; left: 90px; top: 950px; display: flex; gap: 36px; font-size: 16px; line-height: 1.4; }
  .features-title { color: var(--orange); font-size: 16px; margin-bottom: 2px; }
  .features ul { list-style: none; }
  .features li::before { content: "\25CF"; font-size: 11px; margin-right: 8px; vertical-align: 2px; }
  .footer-text { position: absolute; left: 90px; top: 1080px; font-size: 15px; line-height: 1.5; color: var(--ink); }
</style>
</head>
<body>
<main class="flyer">
  <svg class="flyer-art" width="820" height="1160" viewBox="0 0 820 1160">
    <defs>
      <linearGradient id="photo-boy" x1="0" y1="0" x2="0" y2="1">
        <stop offset="0" stop-color="#eeeeea"/><stop offset="1" stop-color="#d4d6dc"/>
      </linearGradient>
      <linearGradient id="photo-hood" x1="0" y1="0" x2="0" y2="1">
        <stop offset="0" stop-color="#ecebe8"/><stop offset="1" stop-color="#a9c3dc"/>
      </linearGradient>
      <linearGradient id="photo-pink" x1="0" y1="0" x2="0" y2="1">
        <stop offset="0" stop-color="#f0efec"/><stop offset="1" stop-color="#e6c3e2"/>
      </linearGradient>
      <linearGradient id="photo-girl" x1="0" y1="0" x2="0" y2="1">
        <stop offset="0" stop-color="#ead3e8"/><stop offset="1" stop-color="#b3cde6"/>
      </linearGradient>
    </defs>
    <polygon class="facet" points="0,0 260,0 120,340 0,260" fill="#ffffff" opacity=".6"/>
    <polygon class="facet" points="260,520 520,430 600,760 300,700" fill="#e9e9e9" opacity=".5"/>
    <polygon class="facet" points="0,820 260,760 200,1040 0,1040" fill="#ffffff" opacity=".5"/>
    <polygon class="side-panel" points="560,0 820,0 820,1160 700,1160 640,860 720,560 600,300" fill="var(--dark)"/>
    <polygon class="side-stripe" points="500,0 560,0 620,120 585,120" fill="var(--orange)"/>
    <polygon class="side-stripe" points="760,580 820,650 820,700 790,660" fill="var(--orange)"/>
    <polygon class="footer-band" points="0,1040 820,1000 820,1160 0,1160" fill="var(--orange)"/>
    <polygon class="footer-corner" points="600,1160 820,1040 820,1160" fill="var(--dark)"/>
    <polygon class="footer-accent" points="740,960 820,900 820,940 760,990" fill="var(--orange)"/>
    <g role="img" aria-label="Photo of a boy wearing a navy and white striped long-sleeve bamboo top">
      <polygon points="470,250 555,70 760,70 820,250 760,430 555,430" fill="#fff" stroke="var(--orange)" stroke-width="5"/>
      <polygon points="488,250 566,86 748,86 806,250 748,414 566,414" fill="url(#photo-boy)"/>
    </g>
    <g role="img" aria-label="Photo of a girl in a light blue hooded bamboo top">
      <polygon points="560,500 620,385 760,385 820,500 760,615 620,615" fill="#fff" stroke="var(--orange)" stroke-width="5"/>
      <polygon points="574,500 630,398 750,398 806,500 750,602 630,602" fill="url(#photo-hood)"/>
    </g>
    <g role="img" aria-label="Photo of a girl in a pink hooded bamboo top">
      <polygon points="560,690 610,600 720,600 775,690 720,780 610,780" fill="#fff" stroke="var(--orange)" stroke-width="5"/>
      <polygon points="574,690 618,612 712,612 761,690 712,768 618,768" fill="url(#photo-pink)"/>
    </g>
    <rect class="photo-standing" role="img" aria-label="Photo of a girl standing in a printed pink top and light blue track pants"
          x="640" y="800" width="125" height="335" rx="18" fill="url(#photo-girl)"/>
  </svg>

  <div class="brand">
    <div class="brand-rule"></div>
    <div class="brand-name">LUMORA</div>
  </div>

  <h1 class="headline">
    <div class="headline-top">LUMORA KIDS</div>
    <div class="headline-bottom">CLOTHING</div>
  </h1>

  <div class="web-ribbon">FIND US AT WWW.LUMORA-WEAR.COM</div>

  <p class="intro">Our children's skin is so soft and delicate. Some little ones need extra protection from the sun in a way that cares for their delicate skin</p>

  <section class="need-box">
    <p class="lead">If your little one -</p>
    <ul>
      <li>Has sensitive skin due to medication</li>
      <li>Has a burn or scar that is not sun friendly</li>
      <li>Is sensitive to uncomfortable clothes</li>
      <li>Or is UV sensitive</li>
    </ul>
    <p class="close">Then we might be able to help!</p>
  </section>

  <p class="range">Our Little Lumora range is 100% Australian made bamboo jersey made especially for everyday sun protection</p>

  <p class="promise">Life is for living, bring back fresh air and flowers in clothes from <span class="nowrap">Lumora-wear.com</span><br>
    <strong>Tested by SOLARIS LAB to UPF 50+ protection, we have your head, arms, legs and hands covered for everyday life outside.</strong></p>

  <section class="features">
    <div>
      <div class="features-title">Features:</div>
      <ul><li>High necklines</li><li>Long sleeves</li></ul>
    </div>
    <div>
      <ul><li>Thumb loops for hand cover</li><li>Breathable fabrics</li></ul>
    </div>
  </section>

  <p class="footer-text">See more at www.lumora-wear.com | WE have things for Mum as well.<br>
    24 Harbour Lane | Brightwater Vic 3999 | Call: 03 5550 1234</p>
</main>
</body>
</html>
```